Lively Ledgers - Minimalistic Single Page Web Design

Project: We are in the process of creating a new Corp Identity. Design a website for our company incorporating the Logo recently designed and selected from a ArtMarketo contest. (attached)

Designers: For this project, you need to design a minimalistic single page, modern website. Beside text and image placement, you will also need to describe user interface, how content is presented and so on.
- Design Layout
- Design Image placements (if any)
- Design menu and buttons
- Design menu and buttons placements
- Design content layout
- Design overall effect and feel of website
- Design color scheme
- Design content style (tone and style of content, words type, how much)
- Design user interface (how do you scroll, what happens when you mouseover buttons, where do certain links and buttons lead you)

Coding Requirements: You need to design the website with a modern perspective on website visuals and effects. Jquery, HTML5 (no FLASH please). You do not need to code for this particular contest, but if you can also code, great, tell me and let me know how I can hire you to complete it. If you know someone that can code your vision, great, let me know. If not, you need to be clear and concise, and be willing to help me communicate with a developer to get the site executed. The web site needs to be modern and dynamic.

Company Name:
Lively Ledgers; Lively-Ledgers; LivelyLedgers

Domain: www.lively-ledgers.com

Company Industry:
Lively Ledgers provides consulting in areas of finance, accounting, business organization, and set up.
- Bookkeeping
- Project Management
- Budget Management
- Cash Management
- Receipt Management
- Filing and Records Management
- Training of administration and accounting staff
- Financial Reports
- Spreadsheets
- Graphs, charts and trend analysis
- Business set up
- Tax filings
- Payroll and HR

Clients:
- Small to medium size businesses
- Proprietors
- Entrepreneurs
- Mom & Pops Shops
- We cater to every industry

Corporate Identity:
- Past: I have never complete a webpage for my company. I did scratch several projects that were started and never completed. I fell in love with stick figures, whimsical designs, similar to that of "Cloudvat", I believed in simplicity and minimalism. However, I was not effective in find the right people to complete my project. Bits and pieces of the website was designed, but never executed.

- Current: I need a webpage design. The web design must align with the current logo aesthetics.The current logo is new. I selected this logo for its simplicity and modern feel. It also incorporated an image of a trending graph, which fits with my company's profile. Still, I am leaning towards simple design, minimalism with boldness. I like my new webpage to be mature and professional, but I want it to portray energy and youth. So no "traditional corp" like design. I like new HTML5 elements, jquery and fun and beautiful forms and buttons. Less image is more.

Note: Please improvise according to your taste and professional perspective, you do not have to follow my suggestions word for word.

Features & Layout:
- Single page layout
- Vertical scroll
- Framed sections so that it looks good on the screen
- Well designed and strategically placed menu bar
- Fills a modern browser
- Beautiful color scheme that pops
- Incorporate Logo aesthetics

Fonts and Type:
- This is an element of the overall design
- I love clean fonts
- Fonts that adds meaning to the overall effect
- Clean

Sounds
- Please no cheesy sounds and background music

Images:
- To your liking
- But please, no lame corp people in suits
- No lame photographs
- I like stick figures
- I like whimsical illustrations

Landing Page:
- This should be the bulk of your design
- The landing page must be impressive, eye catchy
- Bold

Menu Bar:
- Header (introduction and landing page)
- Service & Products
- Company (about us)
- Affiliates and Clients (reference area)
- Contact (contact us area)
- Footer

Colors:
- Up to you, I just like things clean and easy to read
- No black background behind text
- Incorporate Logo Colors

Web Effects:
- According to your liking
- You will need to be involve to communicate the layout and design to the developer, so you need to be clear in your design.

Content:
- You personally don't have to come up with the content, but if you can great.
- I will help come up with the content throughout the contect timeframe, just let me know what you want
- I do not like too much content in my website. The most for each section is 2-3 lines if any.
- Combination could also be one liners.
- I like minimalistic approach.
- If you are not creating the final content, you need to show what type of content need to be created and in what style or tone.

Samples and Inspirations:
- http://singlesheetgallery.example/
- http://vantorix.example/#top
- http://brightmopservices.example/#about
- http://layoutjournal.example/inspiration/23-inspiring-single-page-designs
- http://www.kelvarstudio.example/
- http://www.dariuskessley.example/

This I do not want:
- Too much popups (none if possible)
- Images of people
- Images of people in suits
- Stereotypical images of accountants
- Scrolling marquee
- Clip arts
Updates

Designers, I want to stress the fact that I am looking for a design, not simply a website. The website is 1 page long. Text and content should be minimal. So this means that the design has to do most of the talking. Please do not submit template like web designs, I can pull this off myself if needed. I need you to design a great header, footer and the connecting tissue from landing to end of the page. The entire design needs to flow.

Again, please do not use images of corp people or anything like that. Please think outside the box in how you want to express the company.

Some ideas:
An illustration from beginning to end of the website, have a story.
Add colors to the back ground. 
The background should not get in the way of reading the text, but it does not have to be boring.
Be bold in your design.

Also, please describe more about your design when you submit. Please don't submit a template like design and have no explanation for your actions.

Also, fee free to ask me questions. I am here to help. I check this everyday, so please contact if you need anything.

Designers, please read the details of my post before you submit the design.

If you have a great concept idea but is worry, you can go ahead and submit a pencil draft and ask my opinion before you work anymore on it.

Please see the website samples below for what I am really looking for:

Reason: Hi everyone, I am extending the deadline. It looks like some design are still pending completion, and I want you to have enough time to work on it.

```html
<!DOCTYPE html>
<html lang="en">
<head>
<meta charset="utf-8">
<title>Lively Ledgers</title>
<link href="https://fonts.googleapis.com/css2?family=Open+Sans:wght@400&family=Ubuntu:wght@400;500&family=Mako&display=swap" rel="stylesheet">
<style>
  :root {
    --side-green-dark: #6f8a48;
    --side-green-light: #a4c06a;
    --nav-1: #4b5cf6;
    --nav-2: #3e4cd3;
    --nav-3: #3339ae;
    --nav-4: #282b87;
    --nav-5: #1d1d5a;
    --page-light: #f7f7f7;
    --page-mid: #e2e2e2;
    --brand-navy: #2e3190;
    --brand-green: #8cc63f;
    --accent-rose: #c2285a;
    --ink: #1c1c1c;
    --footer: #000000;
    --white: #ffffff;
  }
  * { box-sizing: border-box; margin: 0; padding: 0; }
  html, body { width: 1200px; height: 720px; overflow: hidden; }
  body { position: relative; background: var(--page-light); font-family: "Mako", sans-serif; }

  .sidebar {
    position: absolute; left: 0; top: 0; width: 94px; height: 720px;
    background: linear-gradient(90deg, var(--side-green-dark), var(--side-green-light));
    border-right: 1px solid #d6d6d6;
  }
  .main-nav { position: absolute; top: 107px; left: 0; width: 94px; list-style: none; }
  .main-nav li {
    height: 94.5px; display: flex; flex-direction: column; align-items: center; justify-content: center;
    color: var(--white); font-family: "Open Sans", sans-serif; font-size: 16px; line-height: 18px;
    text-align: center; text-shadow: 0 1px 2px rgba(0,0,0,.55); letter-spacing: -0.2px;
  }
  .main-nav svg { width: 40px; height: 36px; margin-bottom: 6px; filter: drop-shadow(0 1px 1px rgba(0,0,0,.4)); }
  .nav-home { background: var(--nav-1); }
  .nav-services { background: var(--nav-2); }
  .nav-company { background: var(--nav-3); }
  .nav-affiliates { background: var(--nav-4); }
  .nav-contact { background: var(--nav-5); }

  .stage {
    position: absolute; left: 95px; top: 0; width: 1105px; height: 659px;
    background: radial-gradient(ellipse at 60% 40%, #fbfbfb 0%, #eeeeee 55%, var(--page-mid) 100%);
  }
  .hero-art {
    position: absolute; left: 86px; top: 167px; width: 321px; height: 290px;
    border-radius: 48% 52% 46% 54% / 50% 48% 52% 50%;
    background: radial-gradient(circle at 40% 45%, #f2a23a 0%, #e6457a 30%, #3fa9d9 58%, #7cbf3f 80%, #6b4fa8 100%);
    opacity: .85;
  }
  .hero-shadow {
    position: absolute; left: 180px; top: 486px; width: 180px; height: 12px; border-radius: 50%;
    background: radial-gradient(ellipse, rgba(110,130,150,.45), rgba(110,130,150,0) 70%);
  }
  .brand {
    position: absolute; left: 561px; top: 212px; width: 330px; text-align: center;
    font-family: "Ubuntu", sans-serif; font-weight: 400; font-size: 48px; color: var(--brand-navy);
    letter-spacing: 0.5px;
  }
  .intro { position: absolute; left: 461px; top: 305px; width: 529px; }
  .intro h1 {
    font-family: "Ubuntu", sans-serif; font-weight: 500; font-size: 19px; color: var(--accent-rose);
    text-align: center; letter-spacing: 0.3px; margin-bottom: 12px; padding-left: 18px;
  }
  .intro p { font-size: 15px; line-height: 20.6px; color: var(--ink); text-align: justify; }

  .site-footer {
    position: absolute; left: 95px; top: 659px; width: 1105px; height: 61px; background: var(--footer);
    color: var(--white); font-family: "Open Sans", sans-serif; font-size: 14px;
    display: flex; align-items: center; padding-left: 29px;
  }
</style>
</head>
<body>
  <aside class="sidebar">
    <ul class="main-nav">
      <li class="nav-home">
        <svg viewBox="0 0 40 36"><path d="M20 3 L37 18 L33 18 L33 33 L24 33 L24 23 L16 23 L16 33 L7 33 L7 18 L3 18 Z" fill="#fff"/></svg>
        Home
      </li>
      <li class="nav-services">
        <svg viewBox="0 0 40 36"><circle cx="15" cy="14" r="9" fill="none" stroke="#fff" stroke-width="5" stroke-dasharray="4 2.5"/><circle cx="29" cy="26" r="6" fill="none" stroke="#fff" stroke-width="3.5" stroke-dasharray="3 2"/></svg>
        Services<br>&amp; Products
      </li>
      <li class="nav-company">
        <svg viewBox="0 0 40 36"><circle cx="20" cy="9" r="7" fill="#fff"/><path d="M7 35 Q7 18 20 18 Q33 18 33 35 Z" fill="#fff"/></svg>
        Company
      </li>
      <li class="nav-affiliates">
        <svg viewBox="0 0 40 36"><path d="M3 10 L13 5 L22 14 L18 18 Z M37 10 L27 5 L12 20 L20 28 L26 24 L34 16 Z" fill="#fff"/></svg>
        Affiliates<br>&amp; Clients
      </li>
      <li class="nav-contact">
        <svg viewBox="0 0 40 36"><rect x="3" y="10" width="34" height="22" fill="#fff"/><path d="M3 10 L20 22 L37 10" fill="none" stroke="#1d1d5a" stroke-width="2"/><path d="M3 10 L20 2 L37 10" fill="#fff"/></svg>
        Contact
      </li>
    </ul>
  </aside>

  <main class="stage">
    <div class="hero-art" role="img" aria-label="Speech bubble built from many small colourful figure icons"></div>
    <div class="hero-shadow"></div>
    <div class="brand">livelyledgers</div>
    <section class="intro">
      <h1>LOREM IPSUM DOLOR SIT AMET, CONSECTETUR</h1>
      <p>Ut enim ad minim veniam, quis nostrud exercitation ullamco laboris nisi ut aliquip ex ea commodo consequat. Duis aute irure dolor in reprehenderit in voluptate velit esse cillum dolore eu fugiat nulla pariatur. Excepteur sint occaecat cupidatat non proident, sunt in culpa qui officia deserunt mollit anim</p>
    </section>
  </main>

  <footer class="site-footer">©2013 livelyledgers</footer>
</body>
</html>
```